Power Washing Business Easy Postcard Design

We need a postcard designed for our company, which does residential power washing. We clean houses, decks, driveways and fences. The design should be understated, high end with minimalist graphics. No bubbles or wild colors. The name of the business is "stoneridge power washing" which should be rendered all lower case in a san serif font. Sample files in blue or white are attached. The attached files aren't our logo, just a model. The font doesn't have to be exact and "power washing" needs to be added to it.The postcard size is the Marlo Press 8.64" X 5.59". The photo which is attached should fill the whole front of the card.

The text elements on the front are:
1) "stoneridge power washing"- as per the attached files, can be broken into two lines

2) "Mention this card and receive a FREE standard size Deck Wash"

3) "804-555-3186"

4) "stoneridgepowerwashing.example" (this font size can be smaller than the phone number.)

5)"We Clean:- Houses- Decks- Driveways- Fences"The arrangement is the text is up to you. The text should not overpower the image.

Target Market(s)

Homeowners

Industry/Entity Type

Residential

Font styles to use
Sans Serif

Requirements
Should not have
• Garish graphics

```html
<!DOCTYPE html>
<html lang="en">
<head>
<meta charset="utf-8">
<title>stoneridge power washing postcard</title>
<link rel="stylesheet" href="https://fonts.googleapis.com/css2?family=Arimo:wght@400;700&family=Oswald:wght@500;600&family=Bebas+Neue&display=swap">
<style>
  :root {
    --navy: #1b2f86;
    --navy-deep: #132470;
    --sky: #2b8fe0;
    --green: #8dc63f;
    --red: #e2231a;
    --ink: #111111;
    --white: #ffffff;
    --stage: #2a2a2a;
    --rule: #1f8ad0;
  }
  * { box-sizing: border-box; margin: 0; padding: 0; }
  html, body { width: 1200px; height: 1200px; overflow: hidden; }
  body {
    background: var(--stage);
    font-family: "Arimo", Arial, sans-serif;
    position: relative;
  }

  /* ---------- shared pieces ---------- */
  .brand { color: var(--ink); font-family: "Arimo", Arial, sans-serif; font-weight: 700; line-height: 1; }
  .brand__name { display: block; letter-spacing: -1px; }
  .brand__sub { display: block; letter-spacing: 0.5px; }

  .checklist { list-style: none; }
  .checklist li { display: flex; align-items: center; font-weight: 700; }
  .tick { width: 20px; height: 20px; flex: none; }

  .coupon {
    background: var(--white);
    border: 3px dashed var(--red);
    text-align: center;
    line-height: 1.02;
    color: var(--ink);
  }
  .coupon__lead, .coupon__small { display: block; }
  .coupon__free { display: block; color: var(--red); font-weight: 700; }
  .coupon__item { display: block; color: var(--navy); font-weight: 700; }

  /* ---------- front ---------- */
  .card-front {
    position: absolute; left: 50px; top: 50px;
    width: 860px; height: 580px;
    overflow: hidden; z-index: 2;
    box-shadow: 0 10px 30px rgba(0,0,0,.5);
  }
  .front-photo {
    position: absolute; inset: 0;
    background: linear-gradient(180deg, #4f8fe6 0%, #8fb8ee 28%, #b8a996 52%, #8a6f55 68%, #5a6b3a 84%, #3e5a28 100%);
  }
  .front-panel { position: absolute; inset: 0; width: 860px; height: 580px; }
  .front-brand { position: absolute; left: 24px; top: 44px; }
  .front-brand .brand__name { font-size: 64px; }
  .front-brand .brand__sub { font-size: 32px; margin-top: 2px; }

  .front-side { position: absolute; left: 610px; top: 20px; width: 230px; color: var(--white); text-align: right; }
  .front-side__title {
    font-family: "Oswald", "Arial Narrow", sans-serif; font-weight: 500;
    font-size: 25px; line-height: 1.08; text-transform: uppercase;
  }
  .front-side .checklist { margin-top: 22px; }
  .front-side .checklist li { justify-content: flex-end; font-size: 19px; gap: 6px; margin-bottom: 7px; }
  .front-side .coupon { margin-top: 14px; margin-left: 8px; padding: 8px 6px 8px; }
  .front-side .coupon__lead { font-size: 21px; }
  .front-side .coupon__free { font-size: 50px; }
  .front-side .coupon__small { font-size: 21px; }
  .front-side .coupon__item { font-size: 25px; }

  .front-side-brand { position: absolute; left: 650px; top: 455px; color: var(--white); }
  .front-side-brand .brand__name { font-size: 36px; color: var(--white); }
  .front-side-brand .brand__sub { font-size: 18px; color: var(--white); font-weight: 700; }
  .front-tagline { position: absolute; right: 22px; top: 522px; color: var(--white); font-size: 13px; font-style: italic; font-weight: 700; }

  .front-band { position: absolute; left: 0; bottom: 0; width: 860px; height: 72px; background: var(--green); }
  .call-label {
    position: absolute; left: 22px; top: 488px;
    font-family: "Bebas Neue", "Oswald", sans-serif; font-size: 46px; color: var(--white);
    letter-spacing: 0.5px;
    text-shadow: 0 0 3px var(--navy), 2px 2px 0 var(--navy), -2px -2px 0 var(--navy), 2px -2px 0 var(--navy), -2px 2px 0 var(--navy);
  }
  .call-line { position: absolute; left: 24px; top: 530px; display: flex; align-items: center; gap: 12px; }
  .call-line__icon { width: 52px; height: 40px; }
  .call-line__number { font-family: "Oswald", sans-serif; font-weight: 600; font-size: 44px; color: var(--ink); line-height: 1; }
  .front-url {
    position: absolute; left: 430px; top: 544px;
    font-family: "Arimo", sans-serif; font-weight: 700; font-size: 19px;
    color: var(--red); letter-spacing: 0.3px;
  }

  /* ---------- back ---------- */
  .card-back {
    position: absolute; left: 290px; top: 600px;
    width: 860px; height: 560px;
    background: var(--white); z-index: 1;
    box-shadow: 0 10px 30px rgba(0,0,0,.5);
  }
  .back-topband { position: absolute; left: 0; top: 0; width: 100%; height: 22px; background: var(--rule); }
  .back-spine {
    position: absolute; left: 14px; top: 40px; width: 48px; height: 506px;
    background: var(--navy-deep);
    display: flex; align-items: center; justify-content: center;
  }
  .back-spine__url {
    transform: rotate(-90deg); white-space: nowrap;
    color: var(--white); font-weight: 700; font-size: 19px; letter-spacing: 2px; text-transform: uppercase;
  }
  .back-column {
    position: absolute; left: 62px; top: 40px; width: 388px; height: 506px;
    background: linear-gradient(180deg, #eef3fa 0%, #f6f8fb 55%, #e8eef6 100%);
  }
  .back-photo {
    position: absolute; left: 8px; top: 4px; width: 374px; height: 244px;
    background: linear-gradient(180deg, #4fa1e6 0%, #9dc6ee 38%, #c9a679 56%, #6fae3c 74%, #4a8a26 100%);
  }
  .back-title {
    position: absolute; left: 18px; top: 262px;
    font-family: "Bebas Neue", "Oswald", sans-serif; font-size: 34px; line-height: 1.0;
    color: var(--navy); letter-spacing: 0.5px;
  }
  .back-column .checklist { position: absolute; left: 18px; top: 338px; }
  .back-column .checklist li { font-size: 20px; gap: 6px; margin-bottom: 8px; color: var(--ink); }
  .back-column .coupon { position: absolute; left: 156px; top: 340px; width: 206px; padding: 6px 4px 8px; }
  .back-column .coupon__lead { font-size: 23px; }
  .back-column .coupon__free { font-size: 56px; }
  .back-column .coupon__small { font-size: 22px; }
  .back-column .coupon__item { font-size: 27px; }
  .back-divider { position: absolute; left: 452px; top: 40px; width: 3px; height: 506px; background: #cfd9e6; }
  .stamp-box { position: absolute; right: 40px; top: 66px; width: 96px; height: 100px; border: 2px solid #555; }
  .back-brand { position: absolute; right: 22px; bottom: 36px; text-align: left; }
  .back-brand .brand__name { font-size: 44px; }
  .back-brand .brand__sub { font-size: 22px; margin-top: 2px; }
</style>
</head>
<body>

<svg width="0" height="0" style="position:absolute" aria-hidden="true">
  <defs>
    <symbol id="tick-box" viewBox="0 0 20 20">
      <rect x="1" y="4" width="14" height="14" fill="#ffffff" stroke="#999999" stroke-width="1"/>
      <path d="M3 10 L7 15 L18 1" fill="none" stroke="#e2231a" stroke-width="3" stroke-linecap="round" stroke-linejoin="round"/>
    </symbol>
  </defs>
</svg>

<section class="card-front" aria-label="Postcard front">
  <div class="front-photo" role="img" aria-label="Photo of a large two-storey suburban house lit warmly at dusk with a green lawn"></div>

  <svg class="front-panel" viewBox="0 0 860 580" aria-hidden="true">
    <path d="M640 0 L860 0 L860 508 L590 508 C640 420 630 330 610 230 C595 140 605 60 640 0 Z" fill="var(--navy)"/>
    <path d="M632 0 C597 60 587 140 602 230 C622 330 632 420 582 508" fill="none" stroke="var(--sky)" stroke-width="6"/>
  </svg>

  <div class="brand front-brand">
    <span class="brand__name">stoneridge</span>
    <span class="brand__sub">POWER WASHING</span>
  </div>

  <div class="front-side">
    <h2 class="front-side__title">Safe for<br>environment and<br>landscaping</h2>
    <ul class="checklist">
      <li>Houses <svg class="tick"><use href="#tick-box"/></svg></li>
      <li>Decks <svg class="tick"><use href="#tick-box"/></svg></li>
      <li>Driveways <svg class="tick"><use href="#tick-box"/></svg></li>
      <li>Fences <svg class="tick"><use href="#tick-box"/></svg></li>
    </ul>
    <div class="coupon">
      <span class="coupon__lead">Receive a</span>
      <span class="coupon__free">FREE</span>
      <span class="coupon__small">standard size</span>
      <span class="coupon__item">Deck Wash</span>
      <span class="coupon__small">with this card</span>
    </div>
  </div>

  <div class="brand front-side-brand">
    <span class="brand__name">stoneridge</span>
    <span class="brand__sub">POWER WASHING</span>
  </div>
  <p class="front-tagline">Power &amp; Safe, Effective Cleaning</p>

  <div class="front-band"></div>
  <p class="call-label">CALL US TODAY</p>
  <div class="call-line">
    <svg class="call-line__icon" viewBox="0 0 52 40" aria-hidden="true">
      <path d="M4 12 C4 4 48 4 48 12 L48 16 L38 16 L36 11 L16 11 L14 16 L4 16 Z" fill="var(--ink)"/>
      <path d="M12 18 L40 18 L46 36 L6 36 Z" fill="var(--ink)"/>
      <circle cx="26" cy="27" r="6" fill="var(--green)"/>
    </svg>
    <span class="call-line__number">804-555-3186</span>
  </div>
  <p class="front-url">www.StoneridgePowerWashing.example</p>
</section>

<section class="card-back" aria-label="Postcard back">
  <div class="back-topband"></div>
  <div class="back-spine"><span class="back-spine__url">www.stoneridgepowerwashing.example</span></div>

  <div class="back-column">
    <div class="back-photo" role="img" aria-label="Photo of a smiling family sitting on a lawn in front of a timber house under a blue sky"></div>
    <h2 class="back-title">Safe for environment<br>and landscaping</h2>
    <ul class="checklist">
      <li><svg class="tick"><use href="#tick-box"/></svg> Houses</li>
      <li><svg class="tick"><use href="#tick-box"/></svg> Decks</li>
      <li><svg class="tick"><use href="#tick-box"/></svg> Driveways</li>
      <li><svg class="tick"><use href="#tick-box"/></svg> Fences</li>
    </ul>
    <div class="coupon">
      <span class="coupon__lead">Receive a</span>
      <span class="coupon__free">FREE</span>
      <span class="coupon__small">standard size</span>
      <span class="coupon__item">Deck Wash</span>
      <span class="coupon__small">with this card</span>
    </div>
  </div>
  <div class="back-divider"></div>

  <div class="stamp-box"></div>
  <div class="brand back-brand">
    <span class="brand__name">stoneridge</span>
    <span class="brand__sub">POWER WASHING</span>
  </div>
</section>

</body>
</html>
```